Web Design Project - Coinharbor.com.au

We need a redesign for one of our masthead finance properties, coinharbor.com.au. The new site will feature easy to use tools (calculator etc.) and comparison tables, with an emphasis on sharp, consise content and less clutter.
The redesign should reflect this new approach by appearing clean, polished and professional.
Example Sites for new look and feel:
http://www.yieldnest.com.au/savings-accounts
http://pelto.com.au/savings-accounts/
I've attached a very basic wireframe. Details on different elements as follows:
Find an Account Tool -
Basic redesign of exisiting tool on coinharbor.com.au
Comparsion Table -
To run the size roughly outlined in wireframe, fields to include: Company
Product
Maximum Rate
Interest Earned
Go To Site
Footer -
To include the links currently shown on coinharbor.com.au as well as additional links for 'Banks savings accounts', 'High interest accounts', 'online accounts', 'Interest Rates', 'Saving money tips'
Logo
Please include a logo mock up
Modules -
Should include Image 120x60, headline, short description

```html
<!DOCTYPE html>
<html lang="en">
<head>
<meta charset="utf-8">
<title>Coinharbor.com.au – Savings Accounts</title>
<link rel="stylesheet" href="https://fonts.googleapis.com/css2?family=Open+Sans:wght@300;400;600;700&family=Arimo:wght@400;700&display=swap">
<style>
  :root {
    --page-blue: #1268a5;
    --card-white: #ffffff;
    --row-grey: #f1f1f1;
    --accent-blue: #1b8fd6;
    --ad-blue: #23a0e6;
    --text-dark: #333333;
    --text-body: #505050;
    --text-lead: #444444;
    --rate-grey: #666666;
    --footer-link: #5cc3f3;
    --button-top: #7fd333;
    --button-bottom: #3f9a0c;
  }
  * { box-sizing: border-box; margin: 0; padding: 0; }
  html, body { width: 1200px; height: 706px; overflow: hidden; }
  body {
    background: var(--page-blue);
    position: relative;
    font-family: "Arimo", Arial, sans-serif;
  }
  .card {
    position: absolute;
    background: var(--card-white);
    border-radius: 8px;
  }

  /* comparison table tail */
  .compare-card { left: 120px; top: -10px; width: 640px; height: 88px; }
  .compare-row {
    position: absolute; left: 3px; top: 13px; width: 625px; height: 49px;
    background: var(--row-grey);
  }
  .provider {
    position: absolute; left: 38px; top: 15px;
    font-family: "Open Sans", sans-serif; font-weight: 700; font-size: 11px;
    color: var(--accent-blue); display: flex; align-items: center; gap: 5px;
  }
  .provider-dot { width: 12px; height: 12px; border-radius: 50%; background: var(--accent-blue); }
  .product {
    position: absolute; left: 188px; top: 15px;
    font-family: "Open Sans", sans-serif; font-size: 15px; color: var(--accent-blue);
  }
  .rate {
    position: absolute; left: 388px; top: 7px;
    font-family: "Open Sans", sans-serif; font-size: 24px; color: var(--rate-grey);
  }
  .rate small { font-size: 18px; }
  .site-button {
    position: absolute; left: 518px; top: 9px; width: 106px; height: 30px;
    border-radius: 5px;
    background: linear-gradient(var(--button-top), var(--button-bottom));
    border: 1px solid #3a8a0c;
    color: #fff; font-family: "Open Sans", sans-serif; font-weight: 700; font-size: 14px;
    text-align: center; line-height: 27px; text-decoration: none;
  }

  /* main content */
  .content-card { left: 120px; top: 99px; width: 640px; height: 559px; padding: 24px 30px 0 35px; }
  .content-title {
    font-family: "Open Sans", sans-serif; font-weight: 400; font-size: 25px;
    color: var(--accent-blue); line-height: 32px; margin-bottom: 16px;
  }
  .content-lead {
    font-weight: 700; font-size: 14px; line-height: 16px; color: var(--text-lead);
    margin-bottom: 17px;
  }
  .content-card p.body {
    font-size: 12px; line-height: 16px; color: var(--text-body); margin-bottom: 16px;
  }

  /* side modules */
  .side-card-top { left: 780px; top: -10px; width: 300px; height: 29px; }
  .module { left: 780px; width: 300px; height: 264px; padding: 13px 12px 0 14px; }
  .module-head { display: flex; align-items: center; gap: 13px; margin-bottom: 9px; }
  .ad-slot {
    width: 120px; height: 60px; background: var(--ad-blue); color: #fff;
    font-family: "Open Sans", sans-serif; font-size: 14px;
    display: flex; align-items: center; justify-content: center; flex: none;
  }
  .module-title {
    font-family: "Open Sans", sans-serif; font-weight: 600; font-size: 16px;
    line-height: 15px; color: var(--text-dark);
  }
  .module-text { font-size: 10px; line-height: 14px; color: var(--text-body); padding-left: 4px; }

  /* footer */
  .site-footer {
    position: absolute; left: 118px; top: 678px; width: 958px;
    display: flex; justify-content: space-between; color: #fff;
  }
  .footer-links { font-weight: 700; font-size: 12px; }
  .footer-links a { color: var(--footer-link); text-decoration: none; }
  .footer-links span { color: #fff; padding: 0 2px; }
  .copyright { font-size: 11px; padding-top: 1px; }
</style>
</head>
<body>

<section class="card compare-card">
  <div class="compare-row">
    <div class="provider"><span class="provider-dot"></span>Bayline Credit</div>
    <div class="product">Christmas Club</div>
    <div class="rate">4.25<small>%</small></div>
    <a class="site-button" href="#">Go to site</a>
  </div>
</section>

<main class="card content-card">
  <h1 class="content-title">Welcome to Savings Accounts</h1>
  <p class="content-lead">Lorem ipsum dolor sit amet, consectetur adipiscing elit. Cras quam justo, pharetra a dignissim ut, facilisis nec justo. Sed sodales, leo vulputate varius ultricies, odio turpis placerat ipsum, a pulvinar ipsum massa a sapien.</p>
  <p class="body">Aliquam convallis volutpat mi et mollis. Duis suscipit diam nulla. Morbi tellus diam, aliquet vitae placerat nec, venenatis id magna. Quisque hendrerit, lacus cursus luctus venenatis, odio dui vestibulum odio, sed facilisis tellus odio non nulla. Duis posuere pharetra libero, molestie venenatis nisi facilisis sit amet. Ut eu sapien eu eros mollis pharetra sed vitae erat. Sed consequat placerat eros, semper pellentesque massa bibendum eget. Mauris diam ligula, blandit in aliquam sit amet, scelerisque nec sem. Aliquam eu ipsum nec arcu eleif­end mattis eu eget neque. Mauris mauris turpis, viverra non laoreet nec, vulputate sollicitudin magna.</p>
  <p class="body">Cras felis velit, dapibus placerat accumsan nec, pharetra eget lorem. Phasellus massa ligula, tincidunt vitae ullamcorper posuere, pretium at odio. Fusce arcu risus, placerat sit amet sagittis vel, interdum id libero. Pellentesque dignissim tincidunt vulputate. Vestibulum ante ipsum primis in faucibus orci luctus et ultrices posuere cubilia Curae; Integer neque sapien, scelerisque nec porttitor et, laoreet in mi. Nam sed ipsum sed turpis consequat dapibus quis nec nibh. Suspendisse ipsum lorem, scelerisque a dictum vel, iaculis ut velit. Aliquam pharetra, massa eu posuere tempus, nisi nulla viverra dui, ut fringilla lacus turpis a magna. Vestibu­lum justo ante, tristique a vulputate sed, luctus a tellus. Vestibulum ullamcorper dui non lectus fermentum ut tempor arcu tincidunt. Donec quis hendrerit erat. Ut fringilla tempus leo, sit amet tincidunt lorem tincidunt et. In hac habitasse platea dictumst. Aliquam pulvinar nisi erat, ut consequat augue. Vestibulum feugiat lectus at urna pretium fringilla.</p>
  <p class="body">Morbi sit amet ligula velit. Sed quis volutpat urna. Aenean tincidunt volutpat nisl, eu consequat eros tincidunt nec. Vestibulum tempor ipsum id felis tempus pharetra. Praesent ultricies ultrices cursus. Aliquam quis mauris vel dui dignissim tempus. Nam tristique, justo sed elementum congue, libero leo feugiat mauris, id auctor neque mauris ac orci. Quisque tempor est nec elit rhoncus ac euismod felis vestibulum. Duis nec massa erat, nec luctus enim.</p>
</main>

<aside>
  <div class="card side-card-top"></div>
  <section class="card module" style="top:39px">
    <div class="module-head">
      <div class="ad-slot">120x60px ad</div>
      <h2 class="module-title">Module headline goes here</h2>
    </div>
    <p class="module-text">Lorem ipsum dolor sit amet, consectetur adipiscing elit. Ut sit amet ante blandit leo cursus ornare a nec justo. In pellentesque commodo mauris ac porta. Donec velit quam, dictum nec accumsan ac, volutpat a massa. Donec egestas quam nec libero gravida eleifend. Duis vel erat a lorem suscipit scelerisque at quis eros. Fusce eget justo ac quam pharetra congue et quis nunc. Vivamus tincidunt tempus risus, ut fringilla nisi viverra sit amet. Etiam ac dui ipsum. Fusce vehicula hendrerit pellentesque. Cras placerat gravida felis a ultricies. Praesent tincidunt dapibus risus, a cursus nibh phare­tra ut. Phasellus tellus nibh, posuere at.</p>
  </section>
  <section class="card module" style="top:322px">
    <div class="module-head">
      <div class="ad-slot">120x60px ad</div>
      <h2 class="module-title">Module headline goes here</h2>
    </div>
    <p class="module-text">Lorem ipsum dolor sit amet, consectetur adipiscing elit. Ut sit amet ante blandit leo cursus ornare a nec justo. In pellentesque commodo mauris ac porta. Donec velit quam, dictum nec accumsan ac, volutpat a massa. Donec egestas quam nec libero gravida eleifend. Duis vel erat a lorem suscipit scelerisque at quis eros. Fusce eget justo ac quam pharetra congue et quis nunc. Vivamus tincidunt tempus risus, ut fringilla nisi viverra sit amet. Etiam ac dui ipsum. Fusce vehicula hendrerit pellentesque. Cras placerat gravida felis a ultricies. Praesent tincidunt dapibus risus, a cursus nibh phare­tra ut. Phasellus tellus nibh, posuere at.</p>
  </section>
</aside>

<footer class="site-footer">
  <nav class="footer-links">
    <a href="#">Disclaimer and Terms &amp; Conditions</a><span>|</span><a href="#">Contact Us</a><span>|</span><a href="#">Privacy Policy</a><span>|</span><a href="#">Reviews &amp; Listing Guidelines</a><span>|</span><a href="#">Articles</a><span>|</span><a href="#">News</a>
  </nav>
  <p class="copyright">Copyright 2012 © Coinharbor.com.au.</p>
</footer>

</body>
</html>
```